Business Card Design - cloud video monitoring

For the trade show in Las Vegas our company needs business cards with new brand - Vyrolux

The logo of the new brand is attached, the sample card with the founder's contact details is attached (just change the website to www.vyrolux.me) and email to info@vyrolux.me
Updates

                                        Forgot to say: the tagline for the brand is "the new normal cloud video management"

Industry/Entity Type

Business

```html
<!DOCTYPE html>
<html lang="en">
<head>
<meta charset="utf-8">
<title>Vyrolux Business Card</title>
<link rel="stylesheet" href="https://fonts.googleapis.com/css2?family=Open+Sans:wght@300;400&family=Noto+Serif:wght@400;700&display=swap">
<style>
  :root {
    --page-bg: #e9e6e1;
    --card-dark: #3d3d3f;
    --card-light: #ffffff;
    --accent-teal: #35b99d;
    --name-white: #ffffff;
    --contact-grey: #6e6e70;
  }
  html, body {
    margin: 0;
    width: 1200px;
    height: 900px;
    overflow: hidden;
    background: var(--page-bg);
  }
  .card {
    position: absolute;
    left: 75px;
    top: 150px;
    width: 1050px;
    height: 600px;
    background: var(--card-dark);
    overflow: hidden;
    box-shadow: 0 6px 22px rgba(0,0,0,0.22);
  }
  .card-shape {
    position: absolute;
    inset: 0;
  }
  .brand-dot {
    position: absolute;
    left: 110px;
    top: 165px;
    width: 180px;
    height: 180px;
    border-radius: 50%;
    background: var(--accent-teal);
  }
  .brand-name {
    position: absolute;
    left: 318px;
    top: 118px;
    margin: 0;
    font-family: "Open Sans", sans-serif;
    font-weight: 400;
    font-size: 84px;
    line-height: 1;
    color: var(--accent-teal);
  }
  .person {
    position: absolute;
    left: 338px;
    top: 228px;
    font-family: "Noto Serif", serif;
    color: var(--name-white);
  }
  .person-name {
    font-weight: 700;
    font-size: 30px;
    line-height: 1.2;
    margin: 0;
  }
  .person-role {
    font-weight: 700;
    font-size: 19px;
    margin: 8px 0 0 24px;
  }
  .contact {
    position: absolute;
    font-family: "Open Sans", sans-serif;
    font-weight: 300;
    font-size: 22px;
    line-height: 1.35;
    color: var(--contact-grey);
    margin: 0;
  }
  .contact-phone {
    right: 36px;
    top: 205px;
    text-align: right;
  }
  .contact-web {
    left: 44px;
    bottom: 16px;
  }
</style>
</head>
<body>
  <div class="card">
    <svg class="card-shape" width="1050" height="600" viewBox="0 0 1050 600" aria-hidden="true">
      <path d="M0,470 C420,450 760,330 880,-5 L1050,-5 L1050,600 L0,600 Z" fill="var(--accent-teal)"/>
      <path d="M0,486 C430,468 778,346 900,-5 L1050,-5 L1050,600 L0,600 Z" fill="var(--card-light)"/>
    </svg>

    <span class="brand-dot"></span>
    <p class="brand-name">Vyrolux</p>

    <div class="person">
      <p class="person-name">Mira Kostenko</p>
      <p class="person-role">Founder</p>
    </div>

    <p class="contact contact-phone">Tel: +1 647 555 0142<br>Fax: +1 416 555 0187</p>
    <p class="contact contact-web">Site: www.vyrolux.me<br>Mail: info@vyrolux.me</p>
  </div>
</body>
</html>
```